Fore Sale sign for my real estate agency

I am a Brisbane - Australia inner western suburbs boutique real estate agent who is needing a for sale sign. We are a small dynamic family agency that needs a for sale sign that will standout and give us a strong presence in the market.

I have attached a logo I like, however I am not fixed on anything and am open to suggestions.

The information on the sign should contain but not necessarily limited to the following information - please appreciate I am very open
1 logo - O'Venny
2 Ph number - 3847 1952
3 web address - ovenny.com.au

Thank you
Gareth O'Venny

```html
<!DOCTYPE html>
<html lang="en">
<head>
<meta charset="utf-8">
<title>O'Venny – For Sale Sign</title>
<link rel="stylesheet" href="https://fonts.googleapis.com/css2?family=Alfa+Slab+One&family=Federo&family=Josefin+Sans:wght@600&display=swap">
<style>
  :root {
    --page: #ffffff;
    --card-light: #e9b563;
    --card-mid: #d8962f;
    --card-deep: #b9721c;
    --ink-dark: #2b2420;
    --ink-brown: #5a3418;
    --sale-orange: #d8693a;
    --sale-edge: #7a3a1c;
    --scene-top: rgba(214, 150, 70, 0.35);
    --scene-bottom: rgba(185, 110, 35, 0.55);
    --ornament: #6b3a1f;
  }
  * { margin: 0; padding: 0; box-sizing: border-box; }
  html, body {
    width: 1200px;
    height: 1200px;
    overflow: hidden;
    background: var(--page);
  }
  .canvas {
    position: relative;
    width: 1200px;
    height: 1200px;
    display: flex;
    align-items: center;
    justify-content: center;
  }
  .sign {
    position: relative;
    width: 1040px;
    height: 640px;
    border-radius: 48px;
    overflow: hidden;
    background:
      radial-gradient(ellipse at 55% 40%, var(--card-light) 0%, var(--card-mid) 60%, var(--card-deep) 100%);
  }
  .sign__ornament {
    position: absolute;
    left: 0;
    top: 0;
    width: 210px;
    height: 170px;
    border-bottom-right-radius: 120px;
    background: radial-gradient(circle at 30% 35%, var(--ornament), rgba(107, 58, 31, 0.25) 75%, transparent 100%);
  }
  .sign__scene {
    position: absolute;
    left: 0;
    right: 0;
    top: 300px;
    bottom: 40px;
    background: linear-gradient(180deg, var(--scene-top), var(--scene-bottom));
  }
  .sign__sun {
    position: absolute;
    left: 190px;
    top: 190px;
    width: 320px;
    height: 320px;
    border-radius: 50%;
    background: radial-gradient(circle, rgba(245, 200, 120, 0.55), rgba(245, 200, 120, 0) 70%);
  }
  .brand {
    position: absolute;
    left: 0;
    right: 0;
    top: 70px;
    text-align: center;
    font-family: "Josefin Sans", sans-serif;
    font-weight: 600;
    font-size: 140px;
    line-height: 1;
    color: var(--ink-dark);
    letter-spacing: 2px;
    text-transform: lowercase;
  }
  .headline {
    position: absolute;
    left: 0;
    right: 0;
    top: 230px;
    text-align: center;
    font-family: "Alfa Slab One", serif;
    font-size: 150px;
    line-height: 1;
    color: var(--sale-orange);
    -webkit-text-stroke: 2px var(--sale-edge);
    letter-spacing: 4px;
  }
  .contact {
    position: absolute;
    left: 190px;
    top: 420px;
    color: var(--ink-brown);
    font-family: "Federo", sans-serif;
  }
  .contact__phone {
    font-size: 118px;
    line-height: 1;
    letter-spacing: 2px;
  }
  .contact__web {
    margin-top: 14px;
    margin-left: 40px;
    font-size: 50px;
    line-height: 1;
    letter-spacing: 2px;
    text-transform: uppercase;
  }
</style>
</head>
<body>
  <main class="canvas">
    <section class="sign">
      <div class="sign__sun"></div>
      <div class="sign__scene" role="img" aria-label="Faded illustration of a suburban single-storey house with trees at sunset"></div>
      <div class="sign__ornament" role="img" aria-label="Decorative swirl and leaf ornament"></div>
      <div class="brand">o'venny</div>
      <h1 class="headline">For Sale</h1>
      <div class="contact">
        <div class="contact__phone">3847 1952</div>
        <div class="contact__web">ovenny.com.au</div>
      </div>
    </section>
  </main>
</body>
</html>
```